Tall Birch Path newsletter - Mail Chimp

Tall Birch Path - Empowering Life Coach needs Mail Chimp Newsletter Template. This is a newsletter I will send out monthly to current clients and prospective clients to offer (hopefully) inspiring and uplifting content AND to give info and dates of my upcoming workshops and retreats.

I have attached a word document with all of the different sections of the mail chimp template I would like to have - and hte actual content for the first newsletter.

I'd like to look uplifting, fun, inspiring.

I also need it to be easy for me to use to update in the future :)

Target Market(s)

Women - moms

Industry/Entity Type

Life Coaching

Requirements
Nice to have
• Color theme to match my "Tall Birch Path" logo

```html
<!DOCTYPE html>
<html lang="en">
<head>
<meta charset="utf-8">
<title>Tall Birch Path Newsletter</title>
<link href="https://fonts.googleapis.com/css2?family=Montserrat:wght@500;600;700&family=Lato:wght@400;700&display=swap" rel="stylesheet">
<style>
:root{
  --page:#d3d3ca;
  --card:#ffffff;
  --ink:#1f1f1f;
  --body:#8a8a8a;
  --orange:#f7941d;
  --panel:#f3f3f3;
  --rule:#e2e2e2;
  --link:#c0392b;
}
*{box-sizing:border-box;margin:0;padding:0}
html,body{width:1200px;height:4036px;overflow:hidden}
body{background:var(--page);font-family:"Lato",Arial,sans-serif;color:var(--body);font-size:18px;line-height:25px}
.preheader{text-align:center;padding-top:110px;font-size:17px;line-height:27px;color:#666}
.preheader a{color:var(--link)}
.card{position:absolute;left:231px;top:204px;width:740px;height:3616px;background:var(--card);border-radius:12px;padding:0 30px}
.masthead{display:flex;justify-content:space-between;align-items:flex-end;height:148px;padding:22px 0 18px;border-bottom:2px solid var(--rule)}
.brand{display:flex;align-items:center;gap:12px;font-family:"Montserrat",sans-serif;font-weight:700;font-size:30px;color:#6a3d8f;margin-left:6px}
.brand-dot{width:34px;height:34px;border-radius:50%;background:var(--orange)}
.contact{display:flex;align-items:center;gap:10px;font-family:"Montserrat",sans-serif;font-weight:600;font-size:18px;color:var(--ink)}
.contact-icon{width:44px;height:44px;border-radius:50%;background:var(--orange);display:flex;align-items:center;justify-content:center}
h3{font-family:"Montserrat",sans-serif;font-weight:700;color:var(--ink);font-size:20px;line-height:26px}
.intro{padding-top:44px}
.intro p{margin-bottom:25px}
.intro strong{color:var(--ink)}
.hero{margin-top:30px;height:207px;display:flex}
.hero-photo{flex:0 0 445px;background:linear-gradient(135deg,#f6d36b 0%,#e8a93a 40%,#8a5a2a 100%)}
.hero-side{flex:1;background:linear-gradient(160deg,#2a2a2a,#0e0e0e)}
.section-title{font-family:"Montserrat",sans-serif;font-weight:600;color:var(--orange);font-size:28px;margin:40px 0 0}
.block{padding:0 10px}
.block h3{margin-top:26px}
.block p{margin-top:6px}
.bullets{list-style:none;margin:14px 0}
.bullets li{position:relative;padding-left:26px;margin-bottom:8px}
.bullets li::before{content:"";position:absolute;left:2px;top:7px;width:12px;height:12px;border-radius:50%;background:#bbb}
.tipbox{margin-top:42px;background:var(--panel);border-bottom:6px solid var(--orange);display:flex;align-items:center;height:300px;padding:0 16px}
.tipbox-text{flex:1;padding-right:14px}
.tipbox-text h3{font-size:21px;line-height:27px}
.tipbox-text p{margin-top:10px}
.quote-a{width:158px;height:232px;background:linear-gradient(180deg,#2d3742,#46525e);margin-right:10px}
.quote-b{width:232px;height:232px;background:linear-gradient(180deg,#f4f2ef,#e6e2dc);border:1px solid #ddd}
.events{display:flex;align-items:center}
.events p{flex:1}
.partner-badge{width:70px;height:70px;border-radius:50%;background:#7d5ca8;margin:0 70px 0 30px}
.cta{margin-top:38px;position:relative;background:var(--panel);height:592px}
.cta-band{background:var(--orange);height:188px;clip-path:polygon(0 0,100% 0,100% 72%,0 100%);padding:26px 26px;font-family:"Montserrat",sans-serif;font-weight:700;color:var(--ink);font-size:19px;line-height:25px}
.cta-band a{color:#fff}
.cta-body{padding:38px 32px 0}
.cta-body h3{font-size:20px;line-height:27px}
.quote-c{margin-top:40px;width:234px;height:231px;background:linear-gradient(180deg,#e4e2dc,#bdb9b0);border:4px solid #222}
.footer{position:absolute;left:30px;right:30px;bottom:40px;display:flex;justify-content:space-between;align-items:flex-end}
.footer-brand{font-family:"Montserrat",sans-serif;font-weight:700;color:var(--ink);font-size:18px;margin-bottom:10px}
.follow{text-align:center;font-family:"Montserrat",sans-serif;font-weight:700;color:var(--ink);font-size:15px}
.social{display:flex;gap:8px;margin-top:6px}
.social span{width:36px;height:36px;border-radius:50%;border:2px solid #bbb}
</style>
</head>
<body>
<div class="preheader">Is this email not displaying correctly?<br><a href="#">View it in your browser.</a></div>

<main class="card">
  <header class="masthead">
    <div class="brand"><span class="brand-dot"></span>Tall Birch Path</div>
    <div class="contact">
      <span class="contact-icon">
        <svg width="20" height="14" viewBox="0 0 20 14"><rect x="0" y="0" width="20" height="14" rx="2" fill="#1f1f1f"/><path d="M1 1l9 7 9-7" stroke="#f7941d" stroke-width="1.6" fill="none"/></svg>
      </span>
      dana@tallbirchpath.com
    </div>
  </header>

  <section class="intro">
    <h3>Hello Friends!!</h3>
    <p>I am excited to (hopefully) add a little love to your in-box with this newsletter. I love connecting with moms and helping them find tools to make their lives happier, more intentional, and more fun and this is a new way to do that!</p>
    <p>If you don't know me well, I am a certified Open Horizons Trainer and I lead coaching groups for moms. My OH workshops and Bright Moms Coaching Circle have the goal of fostering connections between amazing women and empowering moms with tools to build lives they are enthusiastic about living, on purpose – and that will be the goal of this newsletter, as well!</p>
    <p>I hope you find something useful and helpful and enjoy receiving this info (and if not, feel free to unsubscribe and my feelings will not be hurt!</p>
    <p>With love,<br><strong>Dana</strong></p>
  </section>

  <div class="hero">
    <div class="hero-photo" role="img" aria-label="Photo of hands forming a heart shape against a warm sunset sky"></div>
    <div class="hero-side" role="img" aria-label="Dark panel with the newsletter name"></div>
  </div>

  <h2 class="section-title">Tall Birch Path Tips &amp; Tools:</h2>

  <section class="block">
    <h3>Building Happiness</h3>
    <p>I firmly believe that thinking about your happiness is important and that happiness itself is a worthwhile goal! If you think about all the things you focus on in your life and all the goals you set for yourself, all of those things are leading you toward feeling happier. Happiness, in the end, is the ultimate goal.</p>
    <p style="margin-top:25px">Of course, what makes each person happy is totally different – and that's awesome and one part of what makes life fun and exciting! Many happiness experts and authors note that the key ingredients in our lives that will make us happier are pursuing 2 categories:</p>
    <ul class="bullets">
      <li>things that bring us pleasure (positive emotions) and</li>
      <li>things that bring us meaning &amp; fulfillment</li>
    </ul>
    <p>Give yourself a minute to think about (it's extra powerful if you write it down!) what makes YOU happy.</p>

    <h3 style="margin-top:44px">What are things that make you feel happy / provide you with pleasure (little and big things!)?</h3>
    <p>For me: joking &amp; laughing with my kids &amp; husband, petting with my dog, sitting with a soft blanket and a book, my first sip of coffee in the morning, walking in nature, traveling, scuba diving, exercise classes, making my friends laugh.</p>

    <h3 style="margin-top:40px">What are things that are meaningful to you / make you feel fulfilled (little and big things!)?</h3>
    <p>For me: teaching Open Horizons workshops, spending quality time with my family, making gratitude lists, volunteering, leading moms' coaching groups, making my kids breakfast.</p>
  </section>

  <div class="tipbox">
    <div class="tipbox-text">
      <h3>How could you add more of those things that bring you happiness to your days?</h3>
      <p>Try to add 1 or 2 of those things per week and see how your happiness increases! You are worth it!</p>
    </div>
    <div class="quote-a" role="img" aria-label="Quote card about designing happiness in the present"></div>
    <div class="quote-b" role="img" aria-label="Quote card about happiness found in the simplest of things"></div>
  </div>

  <section class="block">
    <h3 style="margin-top:40px">Empowering Books:</h3>
    <p>I love to read uplifting, inspiring material. Each newsletter, I'll suggest a few books that I've enjoyed!<br>The Joy Ledger by Marian Holt<br>You Are Enough. How to Quiet Your Inner Critic and Start Living a Brighter Life" by Tess Arlow</p>

    <h3 style="margin-top:34px">Upcoming Events:</h3>
    <div class="events">
      <p>I lead an Open Horizons Workshop 2-3 times per year. The next one is coming up in September/October. More details to come – but here is a little info…</p>
      <span class="partner-badge" role="img" aria-label="Open Horizons badge"></span>
    </div>

    <h3 style="margin-top:40px">Moms - Back to School, Back to You!</h3>
    <p>In September, the kids will be going back to school and you can spend time focusing on YOU. Let this be the year where you take time to focus on yourself so that you can feel amazing, focused, fulfilled, purposeful, and happier! Take the time to learn some simple tools to help you live a life you love, deliberately, instead of just juggling what comes at you and juggling your to-do list. In this workshop, you will be empowered to build a life you love.</p>
  </section>

  <section class="cta">
    <div class="cta-band">
      Dates: 3 morning workshop - September 27, October 4, October 11 , 9:30 – 12:30<br>
      Dana's home in Cedar Ridge<br>
      Interested? Email me: <a href="#">dana@tallbirchpath.com</a>
    </div>
    <div class="cta-body">
      <h3>Enjoy the rest of Summer Break! Savor each amazing day! How can you add a little more HAPPY to your August?? Make the choice and do it!</h3>
      <div class="quote-c" role="img" aria-label="Quote card about choosing happiness as a life goal"></div>
    </div>
  </section>

  <footer class="footer">
    <div class="footer-brand">TallBirchPath 2018.</div>
    <div class="follow">Please Follow us on
      <div class="social"><span></span><span></span><span></span><span></span></div>
    </div>
  </footer>
</main>
</body>
</html>
```